Business Card Design - Cryotherapy

We need a custom created business card for our company FrostLume Spa. We provide whole body cryotherapy and localized cryotherapy to our clients. Please be creative.
Please see our website for idea's on design.
www.frostlumespa.com
Industry/Entity Type
Business
Contact Information for Business Card
Name, Position, Phone Number, Address, Website, Email
Look and feel
Each slider illustrates characteristics of the customer's brand and the style your logo design should communicate.

```html
<!DOCTYPE html>
<html lang="en">
<head>
<meta charset="utf-8">
<title>FrostLume Spa – Business Card</title>
<link rel="stylesheet" href="https://fonts.googleapis.com/css2?family=Open+Sans:wght@400;600;700&display=swap">
<style>
  :root {
    --spa-green: #0f9150;
    --spa-green-dark: #0b7a43;
    --spa-cyan: #12b5c9;
    --spa-teal: #1fae8a;
    --card-white: #fbfbfb;
    --text-grey: #555a5e;
    --stage: #e9ecea;
  }
  * { margin: 0; padding: 0; box-sizing: border-box; }
  html, body { width: 1200px; height: 780px; overflow: hidden; }
  body {
    background: var(--stage);
    font-family: "Open Sans", Arial, sans-serif;
    display: flex;
    align-items: center;
    justify-content: center;
    gap: 60px;
  }
  .card {
    position: relative;
    width: 520px;
    height: 297px;
    border-radius: 14px;
    overflow: hidden;
    background: var(--card-white);
    box-shadow: 0 6px 18px rgba(0,0,0,.14);
  }
  .card-bands { position: absolute; inset: 0; width: 100%; height: 100%; }

  /* Front */
  .contact-block {
    position: absolute;
    top: 26px;
    right: 150px;
    text-align: right;
    color: var(--text-grey);
    font-size: 12.5px;
    line-height: 1.55;
  }
  .contact-name { color: var(--spa-teal); font-weight: 700; font-size: 21px; line-height: 1.15; }
  .contact-role { font-size: 13px; margin-bottom: 6px; }
  .contact-line { display: flex; justify-content: flex-end; align-items: center; gap: 6px; }
  .contact-icon { width: 13px; height: 13px; }
  .contact-web { color: var(--spa-green); font-weight: 600; }

  .brand-mark {
    position: absolute;
    left: 34px;
    bottom: 44px;
    display: flex;
    align-items: center;
    gap: 10px;
  }
  .brand-dot { width: 16px; height: 16px; border-radius: 50%; background: var(--spa-teal); }
  .brand-name { color: var(--spa-green); font-weight: 600; font-size: 22px; }

  /* Back */
  .back-name {
    position: absolute;
    left: 130px;
    right: 130px;
    top: 50%;
    transform: translateY(-50%);
    text-align: center;
    white-space: nowrap;
    color: var(--spa-green);
    font-weight: 600;
    font-size: 30px;
  }
</style>
</head>
<body>

  <section class="card card-front">
    <svg class="card-bands" viewBox="0 0 520 297" aria-hidden="true">
      <path d="M300 297 C370 200 450 110 520 38 L520 52 C455 122 380 210 318 297 Z" fill="var(--spa-cyan)"/>
      <path d="M334 297 C400 205 470 125 520 72 L520 297 Z" fill="var(--spa-green)"/>
    </svg>

    <div class="brand-mark">
      <span class="brand-dot"></span>
      <span class="brand-name">FrostLume Spa</span>
    </div>

    <div class="contact-block">
      <p class="contact-name">Employee Name</p>
      <p class="contact-role">Director</p>
      <p>2210 Willow Creek Road</p>
      <p>Suite 204</p>
      <p>Maple Grove, IL 60120</p>
      <p class="contact-line">(555) 014-2290
        <svg class="contact-icon" viewBox="0 0 14 14"><rect width="14" height="14" rx="2" fill="var(--spa-teal)"/><path d="M4 3.5 L6 3.5 L6.5 5.5 L5.5 6.3 C6.2 7.6 6.8 8.2 8 8.8 L8.8 7.8 L10.5 8.3 L10.5 10.3 C7 10.3 4 7.3 4 3.5 Z" fill="#fff"/></svg>
      </p>
      <p class="contact-line">info@frostlumespa.com
        <svg class="contact-icon" viewBox="0 0 14 14"><rect width="14" height="14" rx="2" fill="var(--spa-teal)"/><rect x="3" y="4.5" width="8" height="5.5" fill="none" stroke="#fff" stroke-width="1"/><path d="M3 4.5 L7 7.7 L11 4.5" fill="none" stroke="#fff" stroke-width="1"/></svg>
      </p>
      <p class="contact-web">www.frostlumespa.com</p>
    </div>
  </section>

  <section class="card card-back">
    <svg class="card-bands" viewBox="0 0 520 297" aria-hidden="true">
      <path d="M0 0 L55 0 C95 110 95 190 50 297 L0 297 Z" fill="var(--spa-green)"/>
      <path d="M68 0 C110 100 108 200 66 297 L78 297 C122 200 124 100 82 0 Z" fill="var(--spa-cyan)"/>
      <path d="M520 0 L465 0 C425 110 425 190 470 297 L520 297 Z" fill="var(--spa-green)"/>
      <path d="M452 0 C410 100 412 200 454 297 L442 297 C398 200 396 100 438 0 Z" fill="var(--spa-cyan)"/>
    </svg>
    <p class="back-name">FrostLume Spa</p>
  </section>

</body>
</html>
```